Fitness competition business needs a card design

I need a professional business card design using my logo. The card will be horizontal with rounded edges.

Target Market(s)

Female fitness competitors

Industry/Entity Type

Fitness

Contact Information for Business Card

Rose-Lynn Darby
Owner
stagevarno.com
555.301.2187
info@stagevarno.com

Font styles to use
Serif

Colors

Designer to choose colors to be used in the design.

Requirements
Must have
• On the back please add the following:
• Figure
• Bikini
• Physique
• Fitness
Nice to have
• Looking for a very sleek design, contemporary and easy to read.
Should not have
• Should not be difficult to read or be too busy

```html
<!DOCTYPE html>
<html lang="en">
<head>
<meta charset="utf-8">
<title>Stage Varno – Business Card</title>
<link rel="stylesheet" href="https://fonts.googleapis.com/css2?family=PT+Serif:ital,wght@0,400;0,700;1,700&display=swap">
<style>
  :root {
    --bg: #8a8f90;
    --card: #ffffff;
    --red: #e0212b;
    --red-deep: #a9181f;
    --charcoal: #3f4042;
    --slate: #6b6c6e;
    --ink: #333335;
    --rule: #e0212b;
  }
  * { margin: 0; padding: 0; box-sizing: border-box; }
  html, body { width: 1200px; height: 1000px; overflow: hidden; }
  body {
    background: var(--bg);
    font-family: "PT Serif", Georgia, serif;
    position: relative;
  }
  .card {
    position: absolute;
    left: 340px;
    width: 520px;
    height: 300px;
    background: var(--card);
    border-radius: 22px;
    overflow: hidden;
  }
  .card--front { top: 160px; }
  .card--back { top: 520px; }

  .front-swoosh { position: absolute; inset: 0; width: 100%; height: 100%; }
  .brand {
    position: absolute;
    left: 40px;
    top: 118px;
    width: 330px;
    display: flex;
    align-items: center;
    gap: 14px;
  }
  .brand-mark { width: 26px; height: 26px; background: var(--charcoal); flex: none; }
  .brand-name {
    font-weight: 700;
    font-size: 42px;
    color: var(--red);
    letter-spacing: 0.5px;
    white-space: nowrap;
  }

  .rule-h { position: absolute; left: 95px; top: 125px; width: 290px; height: 2px; background: var(--rule); }
  .rule-v { position: absolute; left: 330px; top: 50px; width: 2px; height: 210px; background: var(--rule); }
  .holder-name {
    position: absolute;
    right: 200px;
    top: 90px;
    font-style: italic;
    font-weight: 700;
    font-size: 25px;
    color: var(--ink);
    white-space: nowrap;
  }
  .holder-role {
    position: absolute;
    left: 345px;
    top: 92px;
    font-size: 19px;
    color: var(--ink);
  }
  .contact {
    position: absolute;
    right: 205px;
    top: 138px;
    text-align: right;
    list-style: none;
    font-size: 19px;
    line-height: 25px;
    color: var(--ink);
  }
  .divisions {
    position: absolute;
    left: 350px;
    top: 170px;
    list-style: none;
    font-size: 19px;
    line-height: 23px;
    color: var(--ink);
  }
</style>
</head>
<body>
  <section class="card card--front" aria-label="Card front">
    <svg class="front-swoosh" viewBox="0 0 520 300" aria-hidden="true">
      <defs>
        <linearGradient id="redBand" x1="0" y1="0" x2="1" y2="1">
          <stop offset="0" stop-color="var(--red-deep)"/>
          <stop offset="0.5" stop-color="var(--red)"/>
          <stop offset="1" stop-color="var(--red-deep)"/>
        </linearGradient>
      </defs>
      <path d="M240,0 C370,50 430,170 440,300 L520,300 L520,0 Z" fill="#9a9b9d"/>
      <path d="M270,0 C390,55 445,170 452,300 L520,300 L520,0 Z" fill="var(--charcoal)"/>
      <path d="M330,0 C425,60 468,170 470,300 L520,300 L520,0 Z" fill="url(#redBand)"/>
    </svg>
    <div class="brand">
      <span class="brand-mark"></span>
      <span class="brand-name">Stage Varno</span>
    </div>
  </section>

  <section class="card card--back" aria-label="Card back">
    <p class="holder-name">Rose-Lynn Darby</p>
    <p class="holder-role">Owner</p>
    <div class="rule-h"></div>
    <div class="rule-v"></div>
    <ul class="contact">
      <li>stagevarno.com</li>
      <li>555.301.2187</li>
      <li>info@stagevarno.com</li>
    </ul>
    <ul class="divisions">
      <li>Figure</li>
      <li>Bikini</li>
      <li>Physique</li>
      <li>Fitness</li>
    </ul>
  </section>
</body>
</html>
```